User profile management app in Bootstrap & AngularJS

We have a single page web app with front end built on AngularJS and Bootstrap. There is a navbar on top and about 10 different views (user profile view, user profile edit, update-able list of items, help section, ...). At this point the app has functionality but no graphics or thought-out layout.

Need a designer to take the existing HTML, CSS (or even JS) files and modify and expand them to make the app look good. Find the existing HTML and JS files for the client attached. You'll need to download angular, bootstrap and ng-map libraries separately.

You can experience the code live at https://design.tovq.net/tovqportal.html

The templates provided are text-only but the result should contain a few icons for better visual experience. Some suggested areas for images include device types (email, cell phone, pager, landline phone, ...), status indicators (true/false, on/off, enabled/disabled, ...), navigation (expand/collapse, previous page/next page, ...), file download, CRUD management (add, edit, delete), help popups, etc

The resulting design and code should be mobile-friendly and handicap-accessible (Section 508 compliant).

Font desired: Univers family but not required, otherwise Arial
Only use color from the list provided in the attached file. Colors should not indicate a specific meaning and the whole design should be primarily blue (RGB R0 G103 B198) and white themed.

Allow for banner somewhere on top of page - about 530 x 100 pixels. Allow for a footer with an image on the left and 2-3 sentences of text (copyright, disclaimer, etc).
Updates

Target Market(s)

general public, design for simplicity and ease of use

Industry/Entity Type

Cell Phone

Coding

Coded - Design and coding required

Number of Pages Required

5+ page

Font styles to use
Sans Serif
Other font styles liked:
• Univers family preferred not required otw Arial

Requirements
Must have
• Use blue (RGB R0 G103 B198) and white theme. Must be mobile friendly and handicap-enabled.
• Icons: Use the three stroke weights; light, medium, bold.
• Icons can be designed as outlines or solid silhouettes in two-dimensional form. Icons must be recognizable to a majority of the intended audience. Avoid fine lines and overly complex imagery.

```html
<!DOCTYPE html>
<html lang="en">
<head>
<meta charset="utf-8">
<title>Brand – User Profile</title>
<link rel="stylesheet" href="https://fonts.googleapis.com/css2?family=Open+Sans:wght@400;600;700&display=swap">
<style>
:root{
  --blue:#0567b0;
  --blue-top:#0468b1;
  --blue-label:#0562a6;
  --page:#e4e4e4;
  --panel:#f2f2f2;
  --white:#ffffff;
  --line:#e2e2e2;
  --text:#444a4d;
  --slate:#5b6568;
  --slate-dark:#37454c;
  --lime:#b3c52c;
  --accent-red:#d8362c;
  --ok:#6aab16;
  --bad:#d32424;
  --send:#2a9de0;
  --footer:#141414;
  --footer-text:#8a8a8a;
}
*{box-sizing:border-box;margin:0;padding:0}
html,body{width:1200px;height:979px;overflow:hidden}
body{background:var(--page);font-family:"Open Sans",Arial,sans-serif;color:var(--text);position:relative}
.topbar{height:41px;background:var(--blue-top);color:var(--white);display:flex;align-items:center;justify-content:space-between;padding:0 106px 0 123px}
.brand{font-weight:700;font-size:17px;letter-spacing:.3px}
.account-menu{display:flex;gap:24px;font-size:11px}
.account-menu span{display:flex;align-items:center;gap:4px}
.account-menu svg{width:10px;height:10px}
.hero{position:relative;height:169px;background:linear-gradient(100deg,#284866 0%,#5d7f9f 22%,#3b5d80 40%,#9fb7cd 55%,#3a5f85 70%,#c7d5e2 88%,#8fa8c0 100%)}
.mainnav{position:absolute;left:0;right:0;bottom:0;height:53px;background:rgba(8,54,98,.72);border-bottom:3px solid #0b0f14;padding-left:123px;display:flex}
.nav-item{color:var(--white);font-size:11px;font-weight:600;display:flex;flex-direction:column;align-items:center;justify-content:center;gap:4px}
.nav-item svg{width:17px;height:17px;fill:var(--white)}
.nav-item.active{background:var(--lime);border-bottom:3px solid var(--accent-red);margin-bottom:-3px}
.nav-home{width:82px}
.nav-devices{width:88px}
.nav-locations{width:102px}
.nav-profile{width:82px}
.nav-subscriptions{width:124px}
.nav-alerts{width:94px}
.nav-help{width:78px}
.content{position:absolute;top:240px;left:123px;width:980px}
.panel-left{position:absolute;left:0;top:0;width:478px;height:595px;background:var(--panel)}
.panel-head{height:41px;display:flex;align-items:center;gap:10px;padding-left:12px;color:var(--white);font-weight:600;font-size:14px;text-transform:uppercase}
.panel-head svg{width:19px;height:19px;fill:var(--white)}
.panel-left .panel-head{background:var(--blue)}
.profile{position:absolute;left:13px;top:59px;width:451px;border-collapse:collapse;background:var(--white)}
.profile th{width:193px;background:var(--blue-label);color:var(--white);font-size:12px;font-weight:600;text-align:left;padding-left:17px;height:49.4px;vertical-align:middle}
.profile td{font-size:12.5px;padding-left:17px;border-bottom:1px solid var(--line);border-right:1px solid var(--line)}
.profile tr:last-child th,.profile tr:last-child td{height:64px}
.card{position:absolute;left:503px;width:477px;background:var(--white)}
.card .panel-head{background:var(--slate)}
.groups{top:1px}
.devices{top:265px}
.data{width:100%;border-collapse:collapse}
.data th{background:var(--slate-dark);color:var(--white);font-size:12px;font-weight:600;text-align:left;padding-left:17px;text-transform:uppercase}
.data td{font-size:12.5px;padding-left:17px;border-right:1px solid var(--line);border-bottom:1px solid var(--line);background:#f9f9f9}
.data td:last-child{border-right:0}
.groups .data th{height:49px}
.groups .data td{height:49px}
.devices .data th{height:48px}
.devices .data td{height:62px}
.send{margin-left:auto;margin-right:11px;background:var(--send);color:var(--white);font-size:12.5px;font-weight:400;text-transform:none;padding:3px 14px;border-radius:2px}
.status{display:inline-flex;align-items:center;gap:4px;color:var(--white);font-size:9.5px;padding:6px 7px;border-radius:2px}
.status svg{width:8px;height:8px;fill:var(--white)}
.status.enabled{background:var(--ok)}
.status.disabled{background:var(--bad)}
.footer{position:absolute;left:0;right:0;bottom:0;height:89px;background:var(--footer);color:var(--footer-text);font-size:10px;display:flex;align-items:center;justify-content:center}
</style>
</head>
<body>
<header class="topbar">
  <div class="brand">BRAND</div>
  <div class="account-menu">
    <span><svg viewBox="0 0 10 10"><circle cx="5" cy="5" r="3.5" fill="none" stroke="#fff" stroke-width="2"/></svg>Account ▾</span>
    <span><svg viewBox="0 0 10 10"><circle cx="5" cy="3" r="2.3" fill="#fff"/><path d="M1 10c0-3 2-4.5 4-4.5S9 7 9 10z" fill="#fff"/></svg>Brand Username ▾</span>
  </div>
</header>
<section class="hero" role="img" aria-label="Banner photo of a modern office meeting room with chairs, in blue tones">
  <nav class="mainnav" aria-label="Main">
    <div class="nav-item nav-home active"><svg viewBox="0 0 20 20"><path d="M10 2 1 10h3v8h4v-5h4v5h4v-8h3z"/></svg>Home</div>
    <div class="nav-item nav-devices"><svg viewBox="0 0 20 20"><path d="M1 3h18v14H1zm2 2v10h14V5zm2 2h10v1.5H5zm0 3h10v1.5H5zm0 3h10v1.5H5z"/></svg>Devices</div>
    <div class="nav-item nav-locations"><svg viewBox="0 0 20 20"><path d="M10 1a6 6 0 0 0-6 6c0 5 6 12 6 12s6-7 6-12a6 6 0 0 0-6-6zm0 8.5A2.5 2.5 0 1 1 10 4.5a2.5 2.5 0 0 1 0 5z"/></svg>Locations</div>
    <div class="nav-item nav-profile"><svg viewBox="0 0 20 20"><circle cx="10" cy="6" r="4.5"/><path d="M2 19c0-5 3.5-7.5 8-7.5s8 2.5 8 7.5z"/></svg>Profile</div>
    <div class="nav-item nav-subscriptions"><svg viewBox="0 0 20 20"><circle cx="4" cy="16" r="2.5"/><path d="M2 8a10 10 0 0 1 10 10H9a7 7 0 0 0-7-7zm0-6a16 16 0 0 1 16 16h-3A13 13 0 0 0 2 5z"/></svg>Subscriptions</div>
    <div class="nav-item nav-alerts"><svg viewBox="0 0 20 20"><circle cx="10" cy="10" r="9"/><rect x="8.8" y="4.5" width="2.4" height="7" fill="#0a3a66"/><rect x="8.8" y="13" width="2.4" height="2.4" fill="#0a3a66"/></svg>Alert Log</div>
    <div class="nav-item nav-help"><svg viewBox="0 0 20 20"><circle cx="10" cy="10" r="9"/><path d="M7 8a3 3 0 1 1 4.5 2.6c-1 .6-1.3 1-1.3 2" fill="none" stroke="#0a3a66" stroke-width="2.2"/><rect x="9" y="14" width="2.3" height="2.3" fill="#0a3a66"/></svg>Help</div>
  </nav>
</section>

<main class="content">
  <section class="panel-left">
    <h2 class="panel-head"><svg viewBox="0 0 20 20"><circle cx="10" cy="6" r="4.5"/><path d="M2 19c0-5 3.5-7.5 8-7.5s8 2.5 8 7.5z"/></svg>User Profile</h2>
    <table class="profile">
      <tr><th>FIRST NAME</th><td>Jonah</td></tr>
      <tr><th>LAST NAME</th><td>Pell</td></tr>
      <tr><th>EMAIL ADDRESS</th><td>jonah_pell@mailhub.test</td></tr>
      <tr><th>CITY</th><td>Gotham</td></tr>
      <tr><th>STATE</th><td>American Samoa</td></tr>
      <tr><th>AREA CODE</th><td>40187</td></tr>
      <tr><th>CREDITS</th><td>$1000.00</td></tr>
      <tr><th>PHONE</th><td>001 4870 5561</td></tr>
      <tr><th>BIRTHDATE</th><td>05/10/1987</td></tr>
      <tr><th>LANGUAGES</th><td>French<br>Spanish</td></tr>
    </table>
  </section>

  <section class="card groups">
    <h2 class="panel-head"><svg viewBox="0 0 24 20"><circle cx="12" cy="6" r="3.6"/><circle cx="5" cy="7" r="2.6"/><circle cx="19" cy="7" r="2.6"/><path d="M6 17c0-4 3-6 6-6s6 2 6 6zM0 15c0-3 2-4.5 5-4.5 1 0 1.5.2 2 .4-1.5 1-2 2.5-2 4.1zM24 15c0-3-2-4.5-5-4.5-1 0-1.5.2-2 .4 1.5 1 2 2.5 2 4.1z"/></svg>Groups</h2>
    <table class="data">
      <tr><th style="width:155px">Group Name</th><th style="width:149px">Category</th><th>Type</th></tr>
      <tr><td>Group One</td><td>Category Top</td><td>Group Type Top</td></tr>
      <tr><td>Group Two</td><td>Category Top</td><td>Group Type Top</td></tr>
      <tr><td>Group Three</td><td>Category Top</td><td>Group Type Top</td></tr>
    </table>
  </section>

  <section class="card devices">
    <h2 class="panel-head"><svg viewBox="0 0 20 20"><path d="M1 3h18v14H1zm2 2v10h14V5zm2 2h10v1.5H5zm0 3h10v1.5H5zm0 3h10v1.5H5z"/></svg>Devices<span class="send">Send</span></h2>
    <table class="data">
      <tr><th style="width:191px">Device Identifier</th><th style="width:168px">Delivery Channel</th><th>Status</th></tr>
      <tr><td>jonahpell@northwind.test</td><td>E-mail account</td><td><span class="status enabled"><svg viewBox="0 0 10 10"><path d="M1 5l1.4-1.4L4 5.2 7.6 1.6 9 3 4 8z"/></svg>Enabled</span></td></tr>
      <tr><td>(555)018-2746</td><td>Carrierline</td><td><span class="status disabled"><svg viewBox="0 0 10 10"><path d="M2 .6 5 3.6 8 .6 9.4 2 6.4 5l3 3L8 9.4l-3-3-3 3L.6 8l3-3-3-3z"/></svg>Disabled</span></td></tr>
      <tr><td>jonahpell@northwind.test2</td><td>E-mail account</td><td><span class="status disabled"><svg viewBox="0 0 10 10"><path d="M2 .6 5 3.6 8 .6 9.4 2 6.4 5l3 3L8 9.4l-3-3-3 3L.6 8l3-3-3-3z"/></svg>Disabled</span></td></tr>
      <tr><td>qwrtyu@qwrty.test</td><td>E-mail account</td><td><span class="status enabled"><svg viewBox="0 0 10 10"><path d="M1 5l1.4-1.4L4 5.2 7.6 1.6 9 3 4 8z"/></svg>Enabled</span></td></tr>
    </table>
  </section>
</main>

<footer class="footer">© 2015 Brand. All right reserved.</footer>
</body>
</html>
```